Business card, folder, and other items for LMV
Lakemoor Vale Oncology, PLLC business cards and material
Please show us folder designs that will house these documents as well.
Thanks for all the great designs.
After seeing double sided designs above, we would like to utilize this design feature. Please submit double sided designs. Thank you.
Please show designs of folder and stationery as well. Current designs look very nice. Thanks for the submissions.

```html
<!DOCTYPE html>
<html lang="en">
<head>
<meta charset="utf-8">
<title>Lakemoor Vale Oncology, PLLC — Business Cards</title>
<link rel="stylesheet" href="https://fonts.googleapis.com/css2?family=Roboto:wght@400;700;900&display=swap">
<style>
  :root {
    --bg: #e9e7e4;
    --card: #ffffff;
    --blue: #1f5fb4;
    --blue-light: #4c8fd9;
    --blue-dark: #163f85;
    --grey: #b9bcc0;
    --text: #555a60;
    --muted: #8a8f95;
  }
  * { margin: 0; padding: 0; box-sizing: border-box; }
  html, body { width: 1200px; height: 852px; overflow: hidden; }
  body {
    background: var(--bg);
    font-family: "Roboto", Arial, sans-serif;
    position: relative;
  }
  .card {
    position: absolute;
    width: 480px;
    height: 274px;
    background: var(--card);
    border-radius: 14px;
    overflow: hidden;
    box-shadow: 0 4px 14px rgba(0,0,0,0.18);
  }
  .card--front { left: 110px; top: 96px; }
  .card--back  { left: 610px; top: 482px; }
  .swoosh { position: absolute; left: 0; top: 0; width: 480px; height: 274px; }

  .brand {
    position: absolute;
    display: flex;
    align-items: center;
    gap: 10px;
  }
  .brand__dot {
    width: 58px; height: 58px; border-radius: 50%;
    background: var(--blue);
  }
  .brand__name {
    font-weight: 900;
    color: var(--blue);
    letter-spacing: 1px;
    line-height: 1;
  }
  .card--front .brand { left: 150px; top: 34px; }
  .card--front .brand__name { font-size: 72px; }
  .card--back .brand { left: 66px; top: 142px; }
  .card--back .brand__dot { width: 44px; height: 44px; }
  .card--back .brand__name { font-size: 56px; }

  .person { color: var(--blue); font-weight: 700; font-size: 15px; }
  .person__title { color: var(--muted); font-weight: 400; font-size: 13px; }
  .address { color: var(--text); font-size: 12px; line-height: 1.45; }
  .contact { list-style: none; color: var(--text); font-size: 12px; line-height: 1.7; }
  .contact li { display: flex; align-items: center; gap: 7px; }
  .contact svg { width: 12px; height: 12px; flex: none; }
  .divider { position: absolute; width: 1px; background: var(--grey); }

  .card--front .person { position: absolute; left: 150px; top: 138px; }
  .card--front .address { position: absolute; left: 150px; top: 168px; }
  .card--front .divider { left: 262px; top: 164px; height: 70px; }
  .card--front .contact { position: absolute; left: 276px; top: 160px; }

  .card--back .divider { left: 236px; top: 38px; height: 200px; }
  .card--back .info { position: absolute; left: 254px; top: 40px; }
  .card--back .person { display: block; margin-bottom: 2px; }
  .card--back .person__title { display: block; margin-bottom: 18px; }
  .card--back .address { margin-bottom: 12px; }
</style>
</head>
<body>

<svg width="0" height="0" style="position:absolute">
  <defs>
    <linearGradient id="swoosh-blue" x1="0" y1="0" x2="1" y2="1">
      <stop offset="0" stop-color="#4c8fd9"/>
      <stop offset="1" stop-color="#163f85"/>
    </linearGradient>
    <symbol id="icon-phone" viewBox="0 0 12 12">
      <path d="M2.5 1 L4.5 1 L5 3.5 L3.8 4.5 Q5 7 7.5 8.2 L8.5 7 L11 7.5 L11 9.5 Q10.5 11 9 11 Q1 10 1 2.5 Q1 1 2.5 1 Z" fill="#1f5fb4"/>
    </symbol>
    <symbol id="icon-mail" viewBox="0 0 12 12">
      <circle cx="6" cy="6" r="5" fill="none" stroke="#1f5fb4" stroke-width="1.6"/>
      <circle cx="6" cy="6" r="2" fill="#1f5fb4"/>
    </symbol>
    <symbol id="icon-web" viewBox="0 0 12 12">
      <circle cx="6" cy="6" r="5.2" fill="#4c8fd9"/>
      <path d="M1 6 H11 M6 1 V11" stroke="#fff" stroke-width="0.9"/>
    </symbol>
  </defs>
</svg>

<!-- Card with centred brand -->
<section class="card card--front">
  <svg class="swoosh" viewBox="0 0 480 274" aria-hidden="true">
    <path d="M0 120 Q30 210 140 274 L0 274 Z" fill="var(--grey)"/>
    <path d="M0 140 Q22 215 112 274 L0 274 Z" fill="url(#swoosh-blue)"/>
  </svg>
  <div class="brand">
    <span class="brand__dot"></span>
    <span class="brand__name">LMV</span>
  </div>
  <p class="person">Mara Kherwin, M.D., DABR <span class="person__title">/ President</span></p>
  <p class="address">P.O. Box 2841<br>Ridgeway,<br>KY 41209-2841</p>
  <span class="divider"></span>
  <ul class="contact">
    <li><svg><use href="#icon-phone"/></svg>1-606-555-0142</li>
    <li><svg><use href="#icon-mail"/></svg>mkherwin@lakemoorvaleonc.com</li>
    <li><svg><use href="#icon-web"/></svg>www.lakemoorvaleonc.com</li>
  </ul>
</section>

<!-- Card with side brand -->
<section class="card card--back">
  <svg class="swoosh" viewBox="0 0 480 274" aria-hidden="true">
    <path d="M0 110 Q28 205 150 274 L0 274 Z" fill="var(--grey)"/>
    <path d="M0 132 Q20 212 118 274 L0 274 Z" fill="url(#swoosh-blue)"/>
  </svg>
  <div class="brand">
    <span class="brand__dot"></span>
    <span class="brand__name">LMV</span>
  </div>
  <span class="divider"></span>
  <div class="info">
    <span class="person">Mara Kherwin, M.D., DABR</span>
    <span class="person__title">President</span>
    <p class="address">P.O. Box 2841<br>Ridgeway, KY 41209-2841</p>
    <ul class="contact">
      <li><svg><use href="#icon-phone"/></svg>1-606-555-0142</li>
      <li><svg><use href="#icon-mail"/></svg>mkherwin@lakemoorvaleonc.com</li>
      <li><svg><use href="#icon-web"/></svg>www.lakemoorvaleonc.com</li>
    </ul>
  </div>
</section>

</body>
</html>
```